INTERNATIONAL SPEAKING BUSINESS FOR WOMEN NEEDS A BROCHURE DESIGN

HEARTWARD CIRCLE IS AN INTERNATIONAL FEMALE NETWORK PROVIDING ITS MEMBERS THE UK'S NUMBER ONE RELATIONSHIP SEMINAR FOR WOMEN.
WE ARE ABOUT TO GO LIVE AGAIN AFTER 18 MONTHS AND ONE OF OUR OFFERINGS AT THIS LIVE EVENT, IS OUR CONNECTION GROWTH PROGRAMME - AND THIS IS WHERE YOU COME IN :)
IM LOOKING FOR AN ELEGANT, EASY AND WARM TO THE EYE BROCHURE WHICH CAPTURES SOME OF OUR BEST TESTIMONIALS AND CLIENTS. WE HAVE THE LOGO, THE IMAGES AND THE COPY . WE JUST NEED YOUR AMAZING CREATIVE TALENT AND SKILL TO PUT IT ALL TOGETHER TO LOOK ELEGANT AND PROFESSIONAL, YET WELCOMING AND INSPIRING.
OUR IDEAL CLIENT IS A SINGLE, SUCCESSFUL, PROFESSIONAL WOMAN WANTING TO FIND A SOLUTION TO HER RELATIONSHIP CHALLENGES. SHE WANTS TO LET GO OF HER FEARS OF PAST RELATIONSHIPS AND ALIGN WITH AN AMAZING RELATIONSHIP. OUR AIM WITH THE BROCHURE IS TO SHOW THEM WHAT WE DO, HOW WE DO IT AND HOW OUR EXISTING CLIENTS HAVE ALREADY DONE THIS.
THIS IS JUST ONE OF MANY CREATIVE WORKS NEEDED TO BE CARRIED OUT OVER THESE NEXT FEW WEEKS
SO WE ARE LOOKING FOR OUR IDEAL CREATIVE PARTNER ! HOPING TO FIND YOU HERE ;)
heartwardcircle-example.com
professional, successful women between 30 and 65 looking to resolve their relationship problems
Speaking Business/ Seminars / webinars/ Relationships Coaching for Women
- Similar to logo and website heartwardcircle-example.com

```html
<!DOCTYPE html>
<html lang="en">
<head>
<meta charset="utf-8">
<title>Heartward Circle – Connection Growth Programme Brochure</title>
<link href="https://fonts.googleapis.com/css2?family=Montserrat:wght@600;700;800&family=Open+Sans:wght@400;600;700&family=Oswald:wght@500&display=swap" rel="stylesheet">
<style>
  :root {
    --pink: #d2336f;
    --pink-soft: #d9719b;
    --ink: #1e1b1d;
    --ink-2: #2b272a;
    --text: #3a3a3a;
    --paper: #ffffff;
    --stage: #d4d4d4;
    --photo-warm-1: #8a6a55;
    --photo-warm-2: #c9a487;
    --photo-cool: #9ea2a8;
  }
  * { box-sizing: border-box; margin: 0; padding: 0; }
  html, body { width: 1200px; height: 1200px; overflow: hidden; }
  body { background: var(--stage); font-family: "Open Sans", sans-serif; color: var(--text); position: relative; }

  .spread { position: absolute; left: 190px; width: 820px; height: 560px; display: flex; box-shadow: 0 6px 18px rgba(0,0,0,.18); }
  .spread--outside { top: 30px; }
  .spread--inside { top: 610px; }
  .panel { position: relative; width: 410px; height: 560px; background: var(--paper); overflow: hidden; }

  /* ---------- Back cover ---------- */
  .back__body { padding: 22px 26px 0 26px; font-size: 8.4px; line-height: 1.38; }
  .back__intro { font-family: "Montserrat", sans-serif; font-weight: 600; font-size: 8.6px; text-transform: uppercase; color: var(--ink); margin-bottom: 6px; }
  .section-title { font-family: "Montserrat", sans-serif; font-weight: 800; color: var(--pink); text-transform: uppercase; font-size: 8.6px; margin-top: 5px; }
  .pill { display: inline-block; background: var(--pink); color: #fff; font-family: "Montserrat", sans-serif; font-weight: 700; font-size: 8.4px; padding: 3px 12px; border-radius: 10px; margin: 7px 0 2px; }
  .back__band { position: absolute; left: 0; right: 0; bottom: 0; height: 186px; background: linear-gradient(180deg, var(--ink-2), var(--ink)); border-top: 6px solid var(--pink); padding: 20px 26px; color: #fff; }
  .band__headline { font-family: "Montserrat", sans-serif; font-weight: 800; text-align: center; font-size: 13px; letter-spacing: .3px; margin-bottom: 12px; }
  .band__sub { font-family: "Montserrat", sans-serif; font-weight: 800; font-size: 11px; margin-bottom: 8px; }
  .band__sub .pill { font-size: 9px; margin: 0 0 0 6px; }
  .band__copy { font-family: "Montserrat", sans-serif; font-weight: 600; font-size: 12px; line-height: 1.35; }
  .band__copy em { color: var(--pink); font-style: normal; font-weight: 800; }
  .band__note { font-size: 7.6px; margin-top: 10px; color: #e6e6e6; }

  /* ---------- Front cover ---------- */
  .front__photo { position: absolute; top: 0; left: 0; width: 410px; height: 330px; }
  .brand { display: flex; align-items: center; gap: 12px; }
  .brand__dot { width: 34px; height: 34px; border-radius: 50%; background: var(--pink); flex: none; }
  .brand__name { font-family: "Oswald", sans-serif; font-weight: 500; color: var(--pink); letter-spacing: .5px; white-space: nowrap; }
  .front__brand { position: absolute; left: 36px; top: 372px; }
  .front__brand .brand__name { font-size: 34px; }
  .front__bar { position: absolute; left: 0; right: 0; top: 470px; height: 40px; background: var(--ink); color: #fff; font-family: "Montserrat", sans-serif; font-weight: 700; font-size: 15px; letter-spacing: 1px; display: flex; align-items: center; justify-content: center; }

  /* ---------- Inside spread ---------- */
  .pink-frame { position: absolute; top: 36px; height: 394px; background: var(--pink-soft); }
  .inside-left .pink-frame { left: 0; width: 410px; }
  .inside-right .pink-frame { left: 0; width: 410px; }
  .content-card { position: absolute; top: 50px; height: 370px; background: var(--paper); }
  .inside-left .content-card { left: 122px; right: 0; padding: 12px 14px 0 12px; }
  .inside-right .content-card { left: 0; right: 122px; padding: 12px 12px 0 14px; }
  .photo-col { position: absolute; top: 70px; display: flex; flex-direction: column; gap: 26px; }
  .inside-left .photo-col { left: 14px; }
  .inside-right .photo-col { right: 14px; }
  .portrait { width: 96px; height: 92px; }
  .portrait--a { background: linear-gradient(135deg, #d9c3a4, #7d8f6a); }
  .portrait--b { background: linear-gradient(135deg, #cfc6bd, #e8e0d4); }
  .portrait--c { background: linear-gradient(135deg, #8d6c5c, #e7dfd8); }
  .portrait--d { background: linear-gradient(135deg, #e4e2df, #6b4e3e); }
  .portrait--e { background: linear-gradient(135deg, #d8dadc, #7c5a46); }
  .portrait--f { background: linear-gradient(135deg, #3d4a5a, #8a6b58); }

  .testimonial { display: grid; grid-template-columns: 24px 1fr; column-gap: 8px; margin-bottom: 9px; }
  .inside-right .testimonial { grid-template-columns: 1fr 24px; }
  .testimonial__num { width: 24px; height: 24px; border-radius: 50%; background: var(--pink); color: #fff; border: 2px solid #fff; box-shadow: 0 0 0 1.5px var(--pink); font-family: "Montserrat", sans-serif; font-weight: 800; font-size: 12px; display: flex; align-items: center; justify-content: center; }
  .testimonial__name { font-family: "Montserrat", sans-serif; font-weight: 800; color: var(--pink); font-size: 8.6px; text-transform: uppercase; }
  .testimonial__meta { font-family: "Montserrat", sans-serif; font-weight: 700; color: var(--ink); font-size: 8.4px; line-height: 1.3; }
  .testimonial__quote { font-size: 6.6px; line-height: 1.38; margin-top: 3px; color: var(--text); }
  .inside-right .testimonial__head { text-align: right; }

  .dark-band { position: absolute; left: 0; right: 0; bottom: 0; height: 130px; background: linear-gradient(180deg, var(--ink-2), var(--ink)); color: #fff; }
  .host { position: absolute; left: 30px; top: 22px; display: flex; align-items: center; gap: 16px; }
  .host__photo { width: 76px; height: 76px; border-radius: 50%; background: radial-gradient(circle at 45% 40%, #c9a487, #6e5446); border: 2px solid #fff; }
  .host__name { font-family: "Montserrat", sans-serif; font-weight: 800; font-size: 15px; }
  .host__role { font-family: "Montserrat", sans-serif; font-weight: 600; font-size: 10px; }
  .band-brand { position: absolute; left: 30px; bottom: 10px; }
  .band-brand .brand__dot { width: 12px; height: 12px; }
  .band-brand .brand__name { font-size: 10px; }
  .band-brand.brand { gap: 6px; }
  .about { position: absolute; left: 28px; right: 28px; top: 24px; }
  .about__title { font-family: "Montserrat", sans-serif; font-weight: 800; font-size: 13px; margin-bottom: 6px; }
  .about__copy { font-family: "Montserrat", sans-serif; font-weight: 700; font-size: 9.4px; line-height: 1.45; }
  .about-brand { position: absolute; right: 22px; top: 24px; }
  .about-brand .brand__dot { width: 12px; height: 12px; }
  .about-brand .brand__name { font-size: 10px; }
  .about-brand.brand { gap: 6px; }
  .inside-right .dark-band { height: 146px; }
  .inside-right .about { top: 56px; }
</style>
</head>
<body>

<!-- Outside spread: back cover + front cover -->
<section class="spread spread--outside">
  <article class="panel back">
    <div class="back__body">
      <p class="back__intro">Immerse yourself with a group of likeminded individuals in a weekly masterclass and get absorbed in some of the most senior relationships content that's changing the lives of thousands of women internationally.</p>
      <h3 class="section-title">What's included:</h3>
      <p>1.Receive full access to the Connection Growth Programme (once a week)<br>2.Gain full access to the network via our private Gatherly group.</p>
      <h3 class="section-title">About the masterclass:</h3>
      <p>Immerse yourself for one hour a week with like-minded individuals from the comfort and safety of your own home.</p>
      <span class="pill">MONDAYS 7PM-8PM</span>
      <h3 class="section-title">Is this programme for me?</h3>
      <p>If you wish to join one of the UK's Top Female Networks for a Life Changing Year but the unlimited programme is out of budget, then the Masterclass Programme is for you. Give yourself that step in between. We've packaged it up so that you can afford it!</p>
      <h3 class="section-title">What will I learn/ get from the programme?</h3>
      <p>Weekly opportunity to have all your burning relationship questions answered<br>Immerse with a powerful network of like-minded women and learn even more<br>Tools to help you overcome past relationship wounds and patterns<br>Deepen your understanding of self-mastery on route to relationship Mastery</p>
    </div>
    <div class="back__band">
      <p class="band__headline">DON'T LET TODAY FINISH HERE.</p>
      <p class="band__sub">SUBSCRIPTION: <span class="pill">£200 A MONTH</span></p>
      <p class="band__copy">Register today and get the first months' worth <em>TODAY.</em> Tomorrow, wake up and watch half a day of the most powerful content for relationships out there. That's half a day of advanced content for only <em>£200.</em></p>
      <p class="band__note">If at any point you wish to cancel your subscription, just give us 30 days notice.</p>
    </div>
  </article>

  <article class="panel front">
    <svg class="front__photo" viewBox="0 0 410 330" role="img" aria-label="Photo of women seated at a seminar, listening attentively">
      <defs>
        <linearGradient id="audience" x1="0" y1="0" x2="1" y2="1">
          <stop offset="0" stop-color="#6b4f42"/>
          <stop offset=".5" stop-color="#b48b74"/>
          <stop offset="1" stop-color="#d9cfc9"/>
        </linearGradient>
      </defs>
      <path d="M0 0 H410 V240 C330 320 140 340 40 250 C12 220 0 170 0 110 Z" fill="url(#audience)" stroke="#d2336f" stroke-width="9"/>
    </svg>
    <div class="brand front__brand">
      <span class="brand__dot"></span>
      <span class="brand__name">HEARTWARD CIRCLE</span>
    </div>
    <div class="front__bar">www.heartwardcircle-example.com</div>
  </article>
</section>

<!-- Inside spread: testimonials -->
<section class="spread spread--inside">
  <article class="panel inside-left">
    <div class="pink-frame"></div>
    <div class="photo-col">
      <div class="portrait portrait--a" role="img" aria-label="Portrait of testimonial member 1"></div>
      <div class="portrait portrait--b" role="img" aria-label="Portrait of testimonial member 2"></div>
      <div class="portrait portrait--c" role="img" aria-label="Portrait of testimonial member 3"></div>
    </div>
    <div class="content-card">
      <div class="testimonial">
        <span class="testimonial__num">1</span>
        <div>
          <p class="testimonial__name">Nadia Collard</p>
          <p class="testimonial__meta">Age-34,<br>(Missing and exploitation coordinator)</p>
          <p class="testimonial__quote">I joined the programme to resolve issues I had carried in my relationships for years. As a result of this work I see things from a new perspective. Old patterns no longer define me, and I finally feel free to move forward with confidence.</p>
        </div>
      </div>
      <div class="testimonial">
        <span class="testimonial__num">2</span>
        <div>
          <p class="testimonial__name">Alice Harrow</p>
          <p class="testimonial__meta">Age-63<br>(Midwife Labour Ward)</p>
          <p class="testimonial__quote">"I honestly didn't know how I would get through the pain of my breakup. Each week the tools helped me feel my emotions and let them go. Slowly I found peace again and began to trust myself. I've loved every minute of it."</p>
        </div>
      </div>
      <div class="testimonial">
        <span class="testimonial__num">3</span>
        <div>
          <p class="testimonial__name">Alexa Stroud</p>
          <p class="testimonial__meta">Age-39<br>(Receptionist For Adult Mental Health)</p>
          <p class="testimonial__quote">I feel incredibly lucky to have found this group of amazing women. The sessions opened my eyes to how I treat myself and others. The tools helped me break old cycles and I now give myself far more compassion and self-love.</p>
        </div>
      </div>
    </div>
    <div class="dark-band">
      <div class="host">
        <div class="host__photo" role="img" aria-label="Portrait of Maya Ellison"></div>
        <div>
          <p class="host__name">MAYA ELLISON</p>
          <p class="host__role">UK's #1 relationship expert for women</p>
        </div>
      </div>
      <div class="brand band-brand">
        <span class="brand__dot"></span>
        <span class="brand__name">HEARTWARD CIRCLE</span>
      </div>
    </div>
  </article>

  <article class="panel inside-right">
    <div class="pink-frame"></div>
    <div class="photo-col">
      <div class="portrait portrait--d" role="img" aria-label="Portrait of testimonial member 4"></div>
      <div class="portrait portrait--e" role="img" aria-label="Portrait of testimonial member 5"></div>
      <div class="portrait portrait--f" role="img" aria-label="Portrait of testimonial member 6"></div>
    </div>
    <div class="content-card">
      <div class="testimonial">
        <div>
          <div class="testimonial__head">
            <p class="testimonial__name">Clara</p>
            <p class="testimonial__meta">Age-42<br>(Hairstylist)</p>
          </div>
          <p class="testimonial__quote">The masterclasses have been a fantastic way of consolidating what I learned. They are a steady, practical way to keep my mindset on track, and every week I leave with something new to apply in my life and relationships.</p>
        </div>
        <span class="testimonial__num">4</span>
      </div>
      <div class="testimonial">
        <div>
          <div class="testimonial__head">
            <p class="testimonial__name">Melissa Grant</p>
            <p class="testimonial__meta">Age-33<br>(Senior Customer Success Manager)</p>
          </div>
          <p class="testimonial__quote">These sessions are like weekly mastery. I finally understand why I kept repeating the same patterns and how to gently change them. I now have the tools to face difficult emotions and accept myself fully for who I am.</p>
        </div>
        <span class="testimonial__num">5</span>
      </div>
      <div class="testimonial">
        <div>
          <div class="testimonial__head">
            <p class="testimonial__name">Marisol Reyes</p>
            <p class="testimonial__meta">Age-38<br>(Director of Luxury Sales)</p>
          </div>
          <p class="testimonial__quote">The series is my most important weekly date with myself. Each session invites a deeper level of understanding and the practical tools help me grow a little more every single day. I am finally ready to welcome a loving partner.</p>
        </div>
        <span class="testimonial__num">6</span>
      </div>
    </div>
    <div class="dark-band">
      <div class="brand about-brand">
        <span class="brand__dot"></span>
        <span class="brand__name">HEARTWARD CIRCLE</span>
      </div>
      <div class="about">
        <p class="about__title">ABOUT MAYA ELLISON</p>
        <p class="about__copy">A playful, vivacious and inspirational facilitator/ relationship specialist committed to guiding individuals through their journey of self-discovery back to love &amp; peace post painful relationships &amp; events.</p>
      </div>
    </div>
  </article>
</section>

</body>
</html>
```